IT Company Business Card Rebranding

We want to modernize our business cards massively. We want to incorporate aspects of our old business card such as the white and geometric design with the blues of another icon. Existing Logo, old business card and icon are all attached.

We are a modern IT company that provides support for new and growing technologies and want our business cards to be modern yet professional.
Updates

Note: Do not use file ICON.png in design. This is just a design we like Added Wednesday, March 9, 2016

Industry/Entity Type

Information Technology

Contact Information for Business Card

Roughly 43 : 26 or 1075 x 650 px

Font styles to use
Serif

Colors
0492cd
3276b5
33a6d7
86cfc6
cfeae6
cee9f5
ffffff

Requirements
Must have
• Modern yet professional
Nice to have
• We would like to incorporate the blues of our existing logo and of the icon provided. Really like the design of the icon.
Should not have
• Too Decorative. Just simple and professional.
• Not have the circle icon, as it is a copyrighted icon, I just like the colors and the geometric design

```html
<!DOCTYPE html>
<html lang="en">
<head>
<meta charset="utf-8">
<title>Nova Arc – Business Card</title>
<link rel="stylesheet" href="https://fonts.googleapis.com/css2?family=Tinos:wght@400;700&display=swap">
<style>
  :root {
    --page-bg: #e9ecef;
    --card-white: #ffffff;
    --card-grey: #e4e6e8;
    --brand-blue: #3276b5;
    --sky-blue: #33a6d7;
    --deep-blue: #0492cd;
    --mint: #86cfc6;
    --mint-pale: #cfeae6;
    --sky-pale: #cee9f5;
    --name-grey: #7c7f83;
    --text-dark: #3a3d40;
  }
  * { margin: 0; padding: 0; box-sizing: border-box; }
  html, body {
    width: 1200px;
    height: 767px;
    overflow: hidden;
    background: var(--page-bg);
  }
  .business-card {
    position: absolute;
    left: 50px;
    top: 51px;
    width: 1100px;
    height: 665px;
    overflow: hidden;
    background: linear-gradient(180deg, var(--card-white) 0%, #f4f5f6 55%, var(--card-grey) 100%);
    box-shadow: 0 6px 24px rgba(0, 0, 0, 0.12);
    font-family: "Tinos", "Times New Roman", serif;
  }
  .side-art {
    position: absolute;
    inset: 0;
    width: 1100px;
    height: 665px;
  }
  .card-content {
    position: absolute;
    inset: 0;
    text-align: center;
  }
  .company-name {
    position: absolute;
    top: 282px;
    left: 0;
    right: 0;
    display: flex;
    justify-content: center;
    align-items: center;
    gap: 26px;
    font-size: 66px;
    line-height: 76px;
    font-weight: 400;
    letter-spacing: 22px;
    color: var(--name-grey);
    text-transform: uppercase;
  }
  .company-mark {
    width: 32px;
    height: 32px;
    background: var(--brand-blue);
  }
  .person-name {
    position: absolute;
    top: 378px;
    left: 0;
    right: 0;
    font-size: 46px;
    line-height: 52px;
    color: var(--name-grey);
    letter-spacing: 1px;
  }
  .person-role {
    position: absolute;
    top: 430px;
    left: 0;
    right: 0;
    font-size: 23px;
    line-height: 28px;
    color: var(--brand-blue);
    letter-spacing: 0.5px;
  }
  .contact-list {
    position: absolute;
    top: 480px;
    left: 395px;
    list-style: none;
  }
  .contact-item {
    display: flex;
    align-items: center;
    height: 38px;
    font-size: 26px;
    color: var(--text-dark);
  }
  .contact-icon {
    width: 36px;
    height: 26px;
    margin-right: 24px;
    fill: var(--brand-blue);
  }
</style>
</head>
<body>
  <div class="business-card">
    <svg class="side-art" viewBox="0 0 1100 665" role="img" aria-label="Geometric faceted circles in teal and blue on both card edges">
      <defs>
        <linearGradient id="leftFill" x1="0" y1="0" x2="0" y2="1">
          <stop offset="0" stop-color="#4fc4b4"/>
          <stop offset="0.45" stop-color="#86cfc6"/>
          <stop offset="0.55" stop-color="#33a6d7"/>
          <stop offset="1" stop-color="#3276b5"/>
        </linearGradient>
        <linearGradient id="rightFill" x1="1" y1="0" x2="0" y2="0.3">
          <stop offset="0" stop-color="#33c0b0" stop-opacity="0.95"/>
          <stop offset="0.55" stop-color="#86cfc6" stop-opacity="0.75"/>
          <stop offset="1" stop-color="#cfeae6" stop-opacity="0"/>
        </linearGradient>
        <linearGradient id="leftFade" x1="0" y1="0" x2="1" y2="0">
          <stop offset="0.55" stop-color="#ffffff" stop-opacity="0"/>
          <stop offset="1" stop-color="#ffffff" stop-opacity="0.55"/>
        </linearGradient>
      </defs>
      <circle cx="-10" cy="330" r="305" fill="url(#leftFill)"/>
      <circle cx="-10" cy="330" r="305" fill="url(#leftFade)"/>
      <circle cx="1110" cy="330" r="290" fill="url(#rightFill)"/>
    </svg>

    <div class="card-content">
      <div class="company-name"><span class="company-mark"></span><span>Nova Arc</span></div>
      <div class="person-name">BRIAN</div>
      <div class="person-role">TECHNICAL SERVICE</div>

      <ul class="contact-list">
        <li class="contact-item">
          <svg class="contact-icon" viewBox="0 0 36 26" aria-hidden="true">
            <path d="M2 10c0-5 7-8 16-8s16 3 16 8l-1 3-7-1-1-4c-4-1-10-1-14 0l-1 4-7 1z"/>
            <rect x="8" y="15" width="20" height="9" rx="2"/>
          </svg>
          <span>5550 142 867</span>
        </li>
        <li class="contact-item">
          <svg class="contact-icon" viewBox="0 0 36 26" aria-hidden="true">
            <path d="M3 3h30v20H3z M6 6v1l12 9 12-9V6z M6 10v10h24V10L18 19z" fill-rule="evenodd"/>
          </svg>
          <span>brian@novaarc.net</span>
        </li>
        <li class="contact-item">
          <svg class="contact-icon" viewBox="0 0 36 26" aria-hidden="true">
            <path d="M18 1 2 14h5v11h8v-7h6v7h8V14h5z"/>
          </svg>
          <span>www.novaarc.net</span>
        </li>
      </ul>
    </div>
  </div>
</body>
</html>
```